Business Card Design Project - Tall Maple

We are looking for a new business card design. Our company name is Tall Maple Communication Solutions. Our primary function is to provide our clients with communication solutions. These solutions include commercial phone systems and T1 and Fiber Internet lines. Another major part of the business is cabling new buildings with CAT5 cable for both data and phone.

Industry/Entity Type

Communication

Requirements
Must have
• The cards need to be two sided and have some bleeding edge color.
Nice to have
• We are going to upload our current logo BUT we are not married to this logo. If you want to incorporate a re-designed logo with the new business card - please feel free to do so. We are looking for a new bold look that is very colorful yet professional.

```html
<!DOCTYPE html>
<html lang="en">
<head>
<meta charset="utf-8">
<title>Tall Maple Communication Solutions – Business Card</title>
<link rel="stylesheet" href="https://fonts.googleapis.com/css2?family=Questrial&family=Open+Sans:ital,wght@1,600&display=swap">
<style>
  :root {
    --navy-deep: #1a1d6b;
    --navy: #2b3192;
    --navy-light: #3a41a8;
    --ink: #1f2478;
    --paper: #ffffff;
    --stage: #ffffff;
    --steel-light: #eef0f3;
    --steel: #c9cdd4;
  }
  * { margin: 0; padding: 0; box-sizing: border-box; }
  html, body {
    width: 1200px; height: 800px; overflow: hidden;
    background: var(--stage);
  }
  .canvas { position: relative; width: 1200px; height: 800px; }

  .card {
    position: absolute;
    overflow: hidden;
    box-shadow: 0 2px 6px rgba(0,0,0,0.18);
  }

  /* Front */
  .card-front {
    left: 76px; top: 164px; width: 504px; height: 296px;
    background: linear-gradient(180deg, var(--navy-light) 0%, var(--navy) 45%, var(--navy-deep) 100%);
  }
  .brand {
    position: absolute;
    display: flex; align-items: center; gap: 14px;
    color: var(--paper);
    font-family: "Questrial", sans-serif;
    font-weight: 400;
  }
  .card-front .brand { left: 150px; top: 122px; font-size: 40px; }
  .brand-dot {
    width: 22px; height: 22px; border-radius: 50%;
    background: var(--paper);
  }

  /* Back */
  .card-back {
    left: 614px; top: 366px; width: 506px; height: 300px;
    background: var(--paper);
  }
  .tower-art {
    position: absolute; right: 0; top: 0; width: 160px; height: 200px;
    background: linear-gradient(180deg, var(--steel-light) 0%, var(--steel) 100%);
  }
  .services {
    position: absolute; left: 156px; top: 54px;
    list-style: none;
    font-family: "Questrial", sans-serif;
    font-variant: small-caps;
    font-size: 21px; line-height: 21px;
    color: var(--ink);
    letter-spacing: 0.3px;
  }
  .contact-band {
    position: absolute; left: 0; bottom: 0; width: 100%; height: 100px;
    background: linear-gradient(180deg, var(--navy) 0%, var(--navy-deep) 100%);
  }
  .card-back .brand { left: 16px; top: 210px; font-size: 26px; gap: 10px; }
  .card-back .brand-dot { width: 16px; height: 16px; }
  .contact {
    position: absolute; right: 22px; top: 222px;
    text-align: right;
    font-family: "Open Sans", sans-serif;
    font-style: italic; font-weight: 600;
    color: var(--paper);
  }
  .contact-web { font-size: 18px; line-height: 24px; }
  .contact-line { font-size: 15px; line-height: 20px; }
</style>
</head>
<body>
<main class="canvas">

  <section class="card card-front" aria-label="Business card front">
    <div class="brand">
      <span class="brand-name">Tall Maple</span>
      <span class="brand-dot"></span>
    </div>
  </section>

  <section class="card card-back" aria-label="Business card back">
    <div class="tower-art" role="img" aria-label="Steel communication tower rising against a white sky"></div>

    <ul class="services">
      <li>Commercial Phone Systems</li>
      <li>Cabling New Buildings</li>
      <li>CAT5 Cable</li>
      <li>Data and Phone</li>
      <li>T1 / Fiber Internet lines</li>
    </ul>

    <div class="contact-band"></div>

    <div class="brand">
      <span class="brand-name">Tall Maple</span>
      <span class="brand-dot"></span>
    </div>

    <address class="contact">
      <div class="contact-web">TallMapleSolutions.com</div>
      <div class="contact-line">(453) 555-0142</div>
      <div class="contact-line">f: (453) 555-0178</div>
    </address>
  </section>

</main>
</body>
</html>
```